smart logo for a small painting company located in rainy Vancouver Bc *

I need a logo design for business cards and vehicle signage that will cover the entire work van.
Colors: I am open minded
Its a residential/commercial painting company.
I live in the rain forest of western canada. Raincity Vancouver Bc.
I want something that makes people think of the environment as Precious.
I would like to see designs from conservative to wild and crazy.

Target Market(s)

high end residential/commercial painting

Industry/Entity Type

Painting And Decorating

Contact Information for Business Card

On the Front, Just the logo with the logo text. the card stock should have no white showing.
On the Back: Copper Finch Coatings Company
Owner:Darel Hunsaker
Phone:604 318 2465
Email:copperfinchcoatings@mailvista.net
Fully insured, Clean, Quality Service.

Logo Text

Copper Finch Coatings Company

Font styles to use
Other font styles liked:
• Axis

Colors

Designer to choose colors to be used in the design.

Requirements
Must have
• My project must have bold colors.
Nice to have
• A tree frog walking through paint and tracking it up the side of a building
• A tree frog being painted by an artist.
• A paisley tree frog.
Should not have
• A beret. This frog isn't french.

```html
<!DOCTYPE html>
<html lang="en">
<head>
<meta charset="utf-8">
<title>Copper Finch Coatings Company – Business Card</title>
<link href="https://fonts.googleapis.com/css2?family=Montserrat:wght@500;600&family=Open+Sans:ital,wght@0,400;1,700&display=swap" rel="stylesheet">
<style>
  :root {
    --page: #ffffff;
    --ink: #ffffff;
    --teal: #1f5a5c;
    --deep-teal: #153f48;
    --olive: #6e7a2c;
    --amber: #c9781e;
    --orange: #c2561c;
    --red: #9c1b12;
    --maroon: #6d0d0b;
    --band: #4caf3a;
  }
  * { margin: 0; padding: 0; box-sizing: border-box; }
  html, body {
    width: 1200px; height: 932px; overflow: hidden;
    background: var(--page);
  }
  .canvas { position: relative; width: 1200px; height: 932px; }

  .card {
    position: absolute; left: 411px; width: 427px; height: 259px;
    border-radius: 21px; overflow: hidden; color: var(--ink);
  }
  .card--front { top: 181px; }
  .card--back { top: 525px; }

  .paint-fill {
    position: absolute; inset: 0;
    background:
      radial-gradient(ellipse 45% 70% at 8% 35%, var(--deep-teal) 0%, transparent 70%),
      radial-gradient(ellipse 40% 50% at 45% 15%, var(--olive) 0%, transparent 75%),
      radial-gradient(ellipse 45% 60% at 55% 55%, var(--amber) 0%, transparent 70%),
      radial-gradient(ellipse 40% 70% at 85% 40%, var(--orange) 0%, transparent 70%),
      radial-gradient(ellipse 50% 60% at 90% 95%, var(--maroon) 0%, transparent 75%),
      linear-gradient(100deg, var(--teal) 0%, #4d6a3a 35%, var(--orange) 65%, var(--red) 100%);
  }

  .brand-mark {
    position: absolute; width: 53px; height: 53px;
    border: 3px solid var(--ink);
  }
  .brand-name {
    position: absolute; font-family: "Montserrat", sans-serif; font-weight: 600;
    letter-spacing: 1px; white-space: nowrap; line-height: 1;
  }
  .brand-tagline {
    position: absolute; font-family: "Montserrat", sans-serif; font-weight: 500;
    white-space: nowrap; line-height: 1; display: flex; align-items: center; gap: 5px;
  }
  .brand-tagline::before, .brand-tagline::after {
    content: ""; display: block; height: 1.5px; background: var(--ink);
  }

  .card--front .brand-mark { left: 187px; top: 14px; }
  .card--front .brand-name { left: 0; right: 0; top: 60px; text-align: center; font-size: 27px; }
  .card--front .brand-tagline { left: 0; right: 0; top: 94px; justify-content: center; font-size: 12px; }
  .card--front .brand-tagline::before, .card--front .brand-tagline::after { width: 16px; }
  .card--front .brand-mark { top: 14px; }

  .card--back .brand-mark { left: 36px; top: 31px; width: 44px; height: 44px; }
  .card--back .brand-name { left: 92px; top: 35px; font-size: 23px; }
  .card--back .brand-tagline { left: 92px; top: 62px; font-size: 11px; }
  .card--back .brand-tagline::before, .card--back .brand-tagline::after { width: 14px; }

  .contact { position: absolute; left: 113px; top: 110px; font-family: "Open Sans", sans-serif; }
  .contact__name { font-style: italic; font-weight: 700; font-size: 20px; line-height: 1.2; }
  .contact__line { font-size: 15px; line-height: 1.35; }
  .contact__line--email { font-size: 13px; }

  .service-band {
    position: absolute; left: 0; right: 0; top: 212px; height: 26px;
    background: var(--band); text-align: center;
    font-family: "Open Sans", sans-serif; font-size: 18px; line-height: 26px;
  }
</style>
</head>
<body>
<main class="canvas">
  <section class="card card--front" aria-label="Business card front">
    <div class="paint-fill" role="img" aria-label="Fluid paint swirls in teal, olive, orange and red"></div>
    <div class="brand-mark" style="top:14px"></div>
    <div class="brand-name" style="top:82px">COPPER FINCH</div>
    <div class="brand-tagline" style="top:116px">COATINGS COMPANY</div>
  </section>

  <section class="card card--back" aria-label="Business card back">
    <div class="paint-fill" role="img" aria-label="Fluid paint swirls in teal, olive, orange and red"></div>
    <div class="brand-mark"></div>
    <div class="brand-name">COPPER FINCH</div>
    <div class="brand-tagline">COATINGS COMPANY</div>
    <div class="contact">
      <p class="contact__name">Darel Hunsaker</p>
      <p class="contact__line">Ph:604 318 2465</p>
      <p class="contact__line contact__line--email">E:copperfinchcoatings@mailvista.net</p>
    </div>
    <p class="service-band">Fully insured, Clean, Quality Service.</p>
  </section>
</main>
</body>
</html>
```